Book Cover Design Project

A non-fiction book on child protection, specifically... keeping young children safe from predators and keeping teenagers safe from themselves.

Title:
Under Our Roof

Subtitle:
A Guide To Keeping Your Children Safe

Author:
Martin Kellerby

```html
<!DOCTYPE html>
<html lang="en">
<head>
<meta charset="utf-8">
<title>Under Our Roof — Martin Kellerby</title>
<link rel="stylesheet" href="https://fonts.googleapis.com/css2?family=Cinzel:wght@400;500&display=swap">
<style>
  :root {
    --night: #222223;
    --night-deep: #1a1a1b;
    --shade: #121213;
    --glow: #5fdde6;
    --glow-deep: #0aa9d6;
    --paper: #ffffff;
    --paper-fade: #d6d6d6;
    --ink: #0d0d0d;
    --ink-soft: #9a9a9a;
    --ink-faint: #5a5a5a;
  }
  * { margin: 0; padding: 0; box-sizing: border-box; }
  html, body { width: 848px; height: 1200px; overflow: hidden; background: var(--night); }
  .cover {
    position: relative;
    width: 848px;
    height: 1200px;
    overflow: hidden;
    font-family: "Cinzel", "Times New Roman", serif;
    background: linear-gradient(180deg, var(--night-deep) 0%, var(--night) 60%, #2c2c2e 100%);
  }
  .artwork {
    position: absolute;
    left: 0; top: 340px;
    width: 848px; height: 585px;
    background:
      radial-gradient(ellipse 130px 260px at 408px 320px, rgba(95,221,230,0.95) 0%, rgba(10,169,214,0.85) 55%, rgba(10,169,214,0) 100%),
      linear-gradient(90deg, #2a2a2b 0%, var(--night) 35%, var(--night) 65%, var(--shade) 100%);
  }
  .title {
    position: absolute;
    top: 50px; left: 0; width: 100%;
    text-align: center;
    color: var(--paper);
    font-weight: 400;
    font-size: 84px;
    line-height: 100px;
    letter-spacing: 4px;
    text-shadow: 0 0 12px rgba(0,0,0,0.6);
  }
  .subtitle {
    position: absolute;
    top: 284px; left: 0; width: 100%;
    text-align: center;
    color: var(--paper);
    font-size: 19px;
    line-height: 28px;
    letter-spacing: 6px;
  }
  .author-band {
    position: absolute;
    left: 0; top: 925px;
    width: 848px; height: 275px;
    background: linear-gradient(180deg, #f2f2f2 0%, var(--paper) 40%, var(--paper-fade) 100%);
    text-align: center;
  }
  .byline {
    padding-top: 28px;
    color: var(--ink-soft);
    font-size: 56px;
    line-height: 60px;
  }
  .author {
    margin-top: 14px;
    color: var(--ink);
    font-size: 60px;
    line-height: 70px;
    letter-spacing: 1px;
  }
  .copyright {
    position: absolute;
    left: 0; bottom: 30px; width: 100%;
    color: var(--ink-faint);
    font-size: 13px;
    letter-spacing: 7px;
  }
</style>
</head>
<body>
  <main class="cover">
    <h1 class="title">UNDER<br>OUR ROOF</h1>
    <p class="subtitle">A GUIDE TO KEEPING YOUR<br>CHILDREN SAFE</p>
    <div class="artwork" role="img" aria-label="Glowing cyan silhouette of a small child standing between two dark shadowed adult head silhouettes"></div>
    <footer class="author-band">
      <p class="byline">BY</p>
      <p class="author">MARTIN KELLERBY</p>
      <p class="copyright">MARTIN KELLERBY 2012 COPYRIGHT</p>
    </footer>
  </main>
</body>
</html>
```